Zarvo! Next Steps?, Bail Bond Company Check-in App , Court date, Court Reminders, Payments

Zarvo!
Next Steps?
WINNER OF THIS CONTEST WILL HAVE OPPORTUNITY TO DESIGN CUSTOMIZE SOME OUR COMPANY PAGES AFTER CONTEST!
Check-in with your Bail agent via pic/video
Receive Court reminders
Make a payments

Basically this app is a portal to 3rd party bail companies.
The idea is for the person whom makes bail downloads the Zarvo app from App Store.
Then they select a bail bond company.
This would be similar to a restaurant, real estate agent, insurance agent,,app where we could populate bail bond companies by client location or by typing in name of bail company.
We would like the ability to customize each bail bond company landing pages but are open to a global concept. when you click the bail bond company location it would have the logos for that company so the bail bond company screens would need to be customizeble
The app will require a photo or video check-in that is date and time
stamped with a gps location stored in check-in history
Check-in can be scheduled or random or voluntary
Voluntary and Scheduled Check-ins would require check-in button
Random would be via alert or text

The app should be able to receive court date updates
The app should allow clients to make payments to bail bond company
we need
ZARVO! landing page
client registration screens, check-in screens, available bail bond company screens for client to choose from
client registration page should include
name
email address
phone number
picture
home address
work address
date of birth
this app is different from our u-trak app. this is a bail bond check-in app for third party bail bond companies.
landing page should be ZARVO! Next Steps?
ZARVO ! Registration
Find your bail bond Company should list bail bond companies near me and search bar for searching bail bond companies by name
Next landing pages would be customizable for the third party bail bond companies
these would include pages for
check-ins via pics/videos
payment page
court reminders
contact information for bail bond companies
Zarvo Pages include
initial landing page
registration page
search bail companies

Bail bond company pages should include
Bali bond company landing page
Use KELNOR BAIL BOND COMPANY as example
contact information for bail company
check-in page
payment page
court reminder page
Updates

Low designer entries

Low designer entries

Sick

Sick

Sick

Target Market(s)

Court Defendants, Probation ,jails, sheriffs, judges, attorneys

Industry/Entity Type

justice, law enforcement, courts,

Requirements
Must have
• Check-in via pic/video, ability to receive court date reminders, make paymentswe need client registration screens, check-in screens, available bail bond company screens for client to choose from
Nice to have
• Professional easy to navigate intuitive customizable to 3rd party bail bond companies, logos,phone numbers etc.
Should not have
• unprofessional graphics,

```html
<!DOCTYPE html>
<html lang="en">
<head>
<meta charset="utf-8">
<title>Zarvo! – Payments</title>
<link rel="stylesheet" href="https://fonts.googleapis.com/css2?family=Roboto:wght@400;500;700&display=swap">
<style>
  :root {
    --page-bg: #e9eaed;
    --screen-bg: #f8f8f8;
    --card-bg: #ffffff;
    --divider: #e3e3e3;
    --ink: #111111;
    --ink-soft: #555555;
    --ink-muted: #7a7a7a;
    --ring-paid: #7fcf8f;
    --ring-rest: #b9bdd6;
    --accent: #4b82e1;
    --input-border: #dcdcdc;
  }
  * { box-sizing: border-box; margin: 0; padding: 0; }
  html, body {
    width: 1200px; height: 2428px; overflow: hidden;
    background: var(--page-bg);
    font-family: "Roboto", Arial, sans-serif;
    color: var(--ink);
  }
  .screen {
    position: absolute; left: 100px; top: 98px;
    width: 1000px; height: 2232px;
    background: var(--screen-bg);
    border-radius: 40px;
    overflow: hidden;
  }
  .abs { position: absolute; }
  .status-time { left: 50px; top: 38px; font-size: 39px; font-weight: 500; }
  .status-icons { right: 50px; top: 44px; }
  .back { left: 50px; top: 146px; }
  .title { left: 140px; top: 137px; font-size: 56px; font-weight: 500; }
  .section-label { left: 50px; font-size: 45px; font-weight: 500; }
  .card {
    left: 0; width: 1000px; background: var(--card-bg);
    border-top: 3px solid var(--divider);
    border-bottom: 3px solid var(--divider);
  }
  .details { top: 393px; height: 782px; }
  .history { top: 1342px; height: 753px; }
  .ring { left: 55px; top: 62px; }
  .ring-value { left: 58px; top: 148px; width: 250px; text-align: center; font-size: 62px; }
  .paid-label { left: 363px; top: 120px; font-size: 45px; }
  .paid-amount { left: 363px; top: 188px; font-size: 56px; }
  .summary-row {
    left: 53px; width: 907px; display: flex; justify-content: space-between;
    font-size: 40px;
  }
  .summary-row .strong { font-weight: 700; font-size: 44px; }
  .amount-input {
    left: 45px; top: 564px; width: 653px; height: 131px;
    border: 3px solid var(--input-border); border-radius: 22px;
    padding-left: 50px; line-height: 125px;
    font-size: 38px; color: var(--ink-muted);
  }
  .pay-button {
    left: 725px; top: 564px; width: 238px; height: 131px;
    background: var(--accent); border-radius: 22px;
    color: #fff; font-size: 38px; font-weight: 500;
    text-align: center; line-height: 131px;
  }
  .table { left: 50px; top: 52px; width: 896px; border-collapse: collapse; }
  .table th {
    font-size: 41px; font-weight: 400; color: var(--ink-soft);
    height: 78px; text-align: left;
  }
  .table td { font-size: 36px; color: var(--ink-soft); height: 81px; }
  .table .num { text-align: right; }
  .col-date { width: 288px; }
  .col-to { width: 230px; }
</style>
</head>
<body>
<main class="screen">
  <div class="abs status-time">9:41</div>
  <svg class="abs status-icons" width="200" height="40" viewBox="0 0 200 40" aria-hidden="true">
    <rect x="0" y="26" width="7" height="10" rx="1.5" fill="#111"/>
    <rect x="11" y="20" width="7" height="16" rx="1.5" fill="#111"/>
    <rect x="22" y="13" width="7" height="23" rx="1.5" fill="#111"/>
    <rect x="33" y="6" width="7" height="30" rx="1.5" fill="#111"/>
    <path d="M60 14a30 30 0 0 1 42 0l-4 4a24 24 0 0 0-34 0z M67 21a20 20 0 0 1 28 0l-4 4a14 14 0 0 0-20 0z M75 29a8 8 0 0 1 12 0l-6 6z" fill="#111"/>
    <rect x="125" y="6" width="60" height="28" rx="7" fill="none" stroke="#111" stroke-width="3"/>
    <rect x="130" y="11" width="50" height="18" rx="3" fill="#111"/>
    <rect x="188" y="15" width="5" height="10" rx="2" fill="#111"/>
  </svg>

  <svg class="abs back" width="60" height="50" viewBox="0 0 60 50" aria-label="Back" role="img">
    <path d="M52 25H10 M28 6 9 25l19 19" fill="none" stroke="#111" stroke-width="6" stroke-linecap="round" stroke-linejoin="round"/>
  </svg>
  <h1 class="abs title">Payments</h1>

  <h2 class="abs section-label" style="top:320px">Bail details</h2>
  <section class="abs card details">
    <svg class="abs ring" width="256" height="256" viewBox="0 0 256 256" aria-hidden="true">
      <circle cx="128" cy="128" r="118" fill="none" stroke="var(--ring-rest)" stroke-width="17"/>
      <circle cx="128" cy="128" r="118" fill="none" stroke="var(--ring-paid)" stroke-width="17"
              stroke-dasharray="556 741.4" transform="rotate(-90 128 128)"/>
    </svg>
    <div class="abs ring-value">75%</div>
    <div class="abs paid-label">Paid</div>
    <div class="abs paid-amount">$3,000.00</div>

    <div class="abs summary-row" style="top:370px"><span>Total bail</span><span class="strong">$4,000.00</span></div>
    <div class="abs summary-row" style="top:455px"><span>Balance</span><span>$1,000.00</span></div>

    <div class="abs amount-input">Enter amout</div>
    <div class="abs pay-button">Pay</div>
  </section>

  <h2 class="abs section-label" style="top:1262px">Payment history</h2>
  <section class="abs card history">
    <table class="abs table">
      <thead>
        <tr><th class="col-date">Date</th><th class="col-to">Paid to</th><th class="num">Amount</th><th class="num">Method</th></tr>
      </thead>
      <tbody>
        <tr><td>02 Dec 2022</td><td>Kelnor B.B.</td><td class="num">$250.00</td><td class="num">Online</td></tr>
        <tr><td>02 Nov 2022</td><td>Kelnor B.B.</td><td class="num">$250.00</td><td class="num">Cash</td></tr>
        <tr><td>02 Oct 2022</td><td>Kelnor B.B.</td><td class="num">$250.00</td><td class="num">Online</td></tr>
        <tr><td>02 Sep 2022</td><td>Kelnor B.B.</td><td class="num">$250.00</td><td class="num">Online</td></tr>
        <tr><td>02 Aug 2022</td><td>Kelnor B.B.</td><td class="num">$250.00</td><td class="num">Cash</td></tr>
        <tr><td>02 Jul 2022</td><td>Kelnor B.B.</td><td class="num">$250.00</td><td class="num">Online</td></tr>
        <tr><td>02 Jun 2022</td><td>Kelnor B.B.</td><td class="num">$250.00</td><td class="num">Online</td></tr>
      </tbody>
    </table>
  </section>
</main>
</body>
</html>
```